Letterhead Design Project

Brightwater Advisory is a newly created boutique consultancy focussing on delivering strategic consulting to medium and large businesses, with a focus on:
- Strategic planning and execution.
- Corporate function optimisation, especially in the areas of finance, commercial, and IT. This includes implementing the right functional design for the needs of the business, and ensuring the right skills.
- Performance management, in particular project governance and control, operational metrics and management reporting.
I have in mind a tag line for the business being:
"Helping business to discover sustainable value."
I am looking for a letterhead design which utilises my new logo on report templates (powerpoint and word), and letterhead.
Knowlepedex defines a mother lode as follows:
"Mother lode is a principal vein or zone of veins of gold or silver ore. The term probably came from a literal translation of the Spanish veta madre, a term common in old Mexican mining. Veta madre, for instance, is the name given to an 11-kilometre-long (6.8 mi) silver vein discovered in 1548 in Guanajuato, New Spain (modern-day Mexico)."
My preference is for black and gold. Logo files are attached in .eps format. All fonts are outlined. The fonts that are used are "Crimson Text" and "Josefin Sans". They are free open source fonts and they are available here: http://www.typorama-lib.example/fonts
Target Market(s)
Medium to large corporates.
Industry/Entity Type
Boutique
Font styles to use
Other font styles liked:
- All fonts are outlined. The fonts that are used are "Crimson Text" and "Josefin Sans". They are free open source fonts and they are available here: http://www.typorama-lib.example/fonts
Look and feel
Each slider illustrates characteristics of the customer's brand and the style your logo design should communicate.

```html
<!DOCTYPE html>
<html lang="en">
<head>
<meta charset="utf-8">
<title>Brightwater Advisory — Letterhead</title>
<link rel="stylesheet" href="https://fonts.googleapis.com/css2?family=Crimson+Text:wght@400;700&display=swap">
<style>
  :root {
    --backdrop: #e4e4e4;
    --paper: #ffffff;
    --ink: #111111;
    --gold: #dca726;
    --footer-text: #ffffff;
  }
  * { box-sizing: border-box; margin: 0; padding: 0; }
  html, body {
    width: 1000px; height: 1200px; overflow: hidden;
    background: var(--backdrop);
  }
  .letterhead {
    position: absolute; left: 90px; top: 20px;
    width: 820px; height: 1160px;
    background: var(--paper);
  }
  .brand {
    position: absolute; top: 42px; left: 0; width: 820px;
    display: flex; justify-content: center; align-items: center; gap: 20px;
  }
  .brand-square {
    width: 72px; height: 72px;
    background: var(--gold);
    flex: none;
  }
  .brand-text {
    display: flex; flex-direction: column; align-items: flex-start;
  }
  .brand-name {
    font-family: "Crimson Text", serif; font-weight: 400;
    color: var(--ink);
    font-size: 40px; line-height: 44px;
    white-space: nowrap;
  }
  .tagline {
    font-family: "Crimson Text", serif; font-weight: 400;
    color: var(--ink);
    font-size: 13px; line-height: 16px; margin-top: 4px;
    font-style: italic;
    white-space: nowrap;
  }
  .footer-band {
    position: absolute; left: 0; bottom: 0;
    width: 820px; height: 100px;
  }
  .footer-info {
    position: absolute; left: 0; bottom: 0; width: 820px; height: 58px;
    font-family: "Crimson Text", serif; font-weight: 700;
    color: var(--footer-text);
  }
  .address {
    display: flex; justify-content: center; align-items: center; gap: 7px;
    font-size: 11px; margin-top: 8px;
  }
  .contacts {
    display: flex; justify-content: center; align-items: center; gap: 30px;
    font-size: 10px; margin-top: 8px;
  }
  .contact { display: flex; align-items: center; gap: 8px; white-space: nowrap; }
  .contact.web { letter-spacing: 1.5px; font-size: 11px; }
  .icon { width: 14px; height: 14px; fill: var(--footer-text); flex: none; }
</style>
</head>
<body>
  <main class="letterhead">
    <header class="brand">
      <div class="brand-square"></div>
      <div class="brand-text">
        <div class="brand-name">Brightwater Advisory</div>
        <div class="tagline">Strategy, performance and lasting value for business</div>
      </div>
    </header>

    <svg class="footer-band" viewBox="0 0 820 100" preserveAspectRatio="none" aria-hidden="true">
      <path d="M0 12 C120 2 240 8 420 18 C560 24 700 20 820 14 L820 26 C700 32 560 34 420 30 C240 22 120 18 0 26 Z" fill="var(--gold)"/>
      <path d="M0 34 C120 26 240 30 420 38 C560 42 700 40 820 36 L820 100 L0 100 Z" fill="var(--ink)"/>
    </svg>

    <footer class="footer-info">
      <div class="address">
        <svg class="icon" viewBox="0 0 16 16"><path d="M8 1 L15 7.5 L13 7.5 L13 15 L3 15 L3 7.5 L1 7.5 Z"/></svg>
        <span>Level 14, 58 Harbour Lane, Southport QLD 4215, AUSTRALIA</span>
      </div>
      <div class="contacts">
        <div class="contact">
          <svg class="icon" viewBox="0 0 16 16"><path d="M1 6 C1 3 15 3 15 6 L12 7.5 L11 5.5 L5 5.5 L4 7.5 Z M4 9 L12 9 L13.5 14 L2.5 14 Z"/></svg>
          <span>+61 7 5550 2194</span>
        </div>
        <div class="contact">
          <svg class="icon" viewBox="0 0 16 16"><path d="M2 5 L4 5 L4 14 L2 14 Z M5 7 L15 7 L15 14 L5 14 Z M7 2 L13 2 L13 6 L7 6 Z"/></svg>
          <span>+61 7 5550 2195</span>
        </div>
        <div class="contact web">
          <svg class="icon" viewBox="0 0 16 16"><path d="M8 1 A7 7 0 1 0 8.01 1 Z M8 2.5 A5.5 5.5 0 0 1 13.4 7.2 L10.9 7.2 C10.8 5.3 10.3 3.7 9.5 2.7 Z M6.5 2.7 C5.7 3.7 5.2 5.3 5.1 7.2 L2.6 7.2 A5.5 5.5 0 0 1 6.5 2.7 Z M6.6 7.2 C6.7 5 7.3 3.2 8 2.6 C8.7 3.2 9.3 5 9.4 7.2 Z M2.6 8.8 L5.1 8.8 C5.2 10.7 5.7 12.3 6.5 13.3 A5.5 5.5 0 0 1 2.6 8.8 Z M6.6 8.8 L9.4 8.8 C9.3 11 8.7 12.8 8 13.4 C7.3 12.8 6.7 11 6.6 8.8 Z M10.9 8.8 L13.4 8.8 A5.5 5.5 0 0 1 9.5 13.3 C10.3 12.3 10.8 10.7 10.9 8.8 Z"/></svg>
          <span>brightwateradvisory.example</span>
        </div>
      </div>
    </footer>
  </main>
</body>
</html>
```